Handelsunternehmen für haltbare Lebensmittel benötigt Webdesign
Zielgruppe
Wir sind ein Hamburger Handelsunternehmen für haltbare Lebensmittel.
Durch diese Website soll ein Interesse geweckt werden zur Zusammenarbeit und womöglich zur Kooperation der verschiedensten Großhändler des Food-Sektors mit der Vornalto GmbH. Endverbraucher können sich aufgrund der Entdeckung unseres Firmennamens informieren wer wir sind und was wir machen.
Aufgabenstellung
Bitte unterstützt uns bei der Erstellung einer Website unserer Unternehmen. Diese Website soll für unsere Firma Vornalto GmbH sein. Bitte deshalb auch nur den Fokus auf Design für die vornalto.de Seite legen.
Ein externer Shop unter dem Namen kelmstrand.de der Produkte der Kelmstrand vertreibt soll zu einem späteren Zeitpunkt folgen. Dieser Link sollte zwingend im Design als link involviert sein.
Dem Anhang beigefügt findet Ihr unsere beiden Logos.
Da sich unsere zweite Marke Kelmstrand in Zukunft durch das Thema Hamburg optisch definieren soll, beachtet bitte das Vornalto themenübergreifend und generisch funktioniert.
Neu**********Um einen stimmungsvollen Gesamteindruck zu erzeugen im Banner, bitten wir um Verwendung moderner, natürlicher Bilder aus den Bereichen Frische und Natur. Durch florale Illustrationen sollen Akzente gesetzt werden und der Look aufgelockert sein.*************Neu
Unsere Zielgruppe sind erfahrene oder nichterfahrene kochbegeisterte Entdecker kulinarischer Genüsse die sich aufgrund der Entdeckung des Firmennamens auf unseren Artikeln des Kelmstrand Portfolios über die Herkunft des Unternehmens informieren möchten. Die Zielgruppe zeichnet sich durch Spontanität und Individualität aus. Werbung gegenüber ist die Zielgruppe sehr aufgeschlossen. Beim Einkauf ist ihnen Qualität wichtiger als der Preis. Sie konsumieren gerne Markenartikel und bevorzugen beim Einkauf eine Inspiration die wir Ihnen über die Website mitgeben werden. Die Umweltverträglichkeit von Produkten spielt für sie eine große Rolle. Nachhaltigkeit ist ihnen wichtig.
Wir wünschen uns einen hohen Wiedererkennungswert der durch unseren internationalen Namen begründet ist und einer europaweiten Expansion nichts im Wege steht.
Es soll ein OnePager werden der auch in der Mobilversion gut funktionieren muss. Also muss die Responsivität sehr gut umgesetzt sein.
Der Firmenauftritt soll grob wie folgt aufgebaut sein:
Home
LOGO(De..

```html
<!DOCTYPE html>
<html lang="de">
<head>
<meta charset="utf-8">
<title>Vornalto</title>
<link href="https://fonts.googleapis.com/css2?family=Montserrat:wght@400;500;600;700&display=swap" rel="stylesheet">
<style>
:root{
  --ink:#1c1d21;
  --ink-2:#1f2024;
  --cream:#e4e1c3;
  --gold:#f0b031;
  --olive:#8d8541;
  --line:#8a8660;
  --white:#ffffff;
  --text-dark:#1a1a1a;
}
*{margin:0;padding:0;box-sizing:border-box}
html,body{width:1200px;height:2862px;overflow:hidden}
body{font-family:'Montserrat',sans-serif;background:var(--ink);color:var(--white);position:relative}
.abs{position:absolute}

/* Hero */
.hero{position:absolute;left:0;top:0;width:1200px;height:675px;
  background:radial-gradient(circle at 1120px 80px,#7a1a14 0,#3a1410 110px,transparent 170px),
  radial-gradient(circle at 1080px 400px,#8a6a1c 0,#4a3a18 150px,transparent 230px),
  radial-gradient(circle at 340px 560px,#b49a1a 0,#5a5015 70px,transparent 100px),
  radial-gradient(circle at 720px 600px,#6a5a2a 0,#3a3020 90px,transparent 130px),
  radial-gradient(circle at 60px 560px,#2f5a22 0,#1a2a18 120px,transparent 180px),
  linear-gradient(#1d2226,#22282c)}
.topbar{top:14px;left:111px;width:978px;height:22px;font-size:11px;letter-spacing:.5px}
.search{left:0;top:0;display:flex;align-items:center;gap:22px}
.mail{right:0;top:2px;display:flex;align-items:center;gap:6px;font-size:11px}
.nav{top:56px;left:111px;width:978px;height:44px;border-top:1px solid #d8d8d8;border-bottom:1px solid #d8d8d8;display:flex}
.nav a{flex:1;color:var(--white);text-decoration:none;font-size:13px;font-weight:500;letter-spacing:2px;display:flex;align-items:center;justify-content:center;border-left:1px solid #d8d8d8}
.nav a:first-child{border-left:none}
.logo-wreath{left:344px;top:205px;width:517px;height:189px;border-radius:90px;background:rgba(255,255,255,.06)}
.logo-plate{left:391px;top:253px;width:418px;height:94px;background:#1d2528;display:flex;align-items:center;justify-content:center;font-size:64px;font-weight:700;letter-spacing:2px}

/* Welcome */
.welcome{left:0;top:675px;width:1200px;height:466px;background:var(--ink-2)}
.welcome-box{left:111px;top:86px;width:978px;height:293px;border:1px solid var(--line);text-align:center;padding:34px 60px 0}
.welcome-box h1{font-size:37px;font-weight:700;margin-bottom:14px}
.welcome-box p{font-size:14px;line-height:20.5px;margin-bottom:20px;font-weight:500}

/* Portfolio */
.portfolio{left:0;top:1141px;width:1200px;height:920px;background:var(--cream);color:var(--text-dark)}
.portfolio h2{position:absolute;top:74px;width:100%;text-align:center;font-size:35px;font-weight:700}
.card{position:absolute;width:224px;height:329px;border:1px solid var(--gold);text-align:center}
.card .photo{position:absolute;left:30px;top:42px;width:164px;height:164px;border-radius:50%;border:4px solid var(--gold);background:var(--white)}
.card h3{position:absolute;top:228px;width:100%;font-size:18px;font-weight:600}
.card .btn{position:absolute;left:35px;top:263px;width:154px;height:31px;background:var(--gold);color:var(--white);font-size:11.5px;font-weight:700;display:flex;align-items:center;justify-content:center;letter-spacing:.3px}

/* Contact */
.contact{left:0;top:2061px;width:1200px;height:615px;background:var(--ink)}
.branch{width:262px;height:274px;top:37px;border-radius:40px;background:linear-gradient(135deg,rgba(255,255,255,.12),rgba(255,255,255,.04))}
.contact-frame{left:111px;top:337px;width:978px;height:191px;border:1px solid var(--line);border-top:none}
.contact h2{position:absolute;top:62px;width:100%;text-align:center;font-size:35px;font-weight:700}
.rule{height:1px;background:var(--line);top:86px}
.gold-dash{left:576px;top:124px;width:48px;height:1px;background:var(--gold)}
.contact .lead{position:absolute;top:149px;width:100%;text-align:center;font-size:14px;font-weight:500;padding-left:14px}
.field{border-bottom:1px solid #cfcfcf;font-size:13.5px;font-weight:500;height:27px}
.join{left:358px;top:387px;width:486px;height:56px;border:2px solid #e0e0e0;display:flex;align-items:center;justify-content:center;font-size:13px}

/* Footer */
.footer{left:0;top:2676px;width:1200px;height:186px;background:var(--olive);font-size:12px}
.footer .rows{left:111px;top:43px;width:978px;height:110px;border-top:1px solid #cfcaa0;border-bottom:1px solid #cfcaa0}
.footnav{left:0;top:0;height:55px;display:flex;align-items:center;font-size:12.5px}
.footnav span{display:inline-block}
.social{right:0;top:15px;display:flex;gap:7px}
.social i{width:27px;height:27px;border-radius:50%;background:#5a5430;display:flex;align-items:center;justify-content:center}
.social i.accent{background:var(--gold)}
.social i.dark{background:#111}
.info{left:0;top:55px;width:978px;height:55px;border-top:1px solid #cfcaa0;display:flex;font-size:11.5px;font-weight:600}
.info div{display:flex;align-items:center;justify-content:center;text-align:center;border-left:1px solid #cfcaa0;line-height:16px}
.info div:first-child{border-left:none}
</style>
</head>
<body>

<header class="hero" role="img" aria-label="Dunkle Tischplatte mit Gewürzen in Schalen, Olivenöl, Pesto, Basilikum und Spaghetti">
  <div class="abs topbar">
    <div class="abs search">
      <svg width="15" height="15" viewBox="0 0 15 15"><circle cx="6" cy="6" r="5" fill="none" stroke="#fff" stroke-width="1.5"/><line x1="9.8" y1="9.8" x2="14" y2="14" stroke="#fff" stroke-width="1.5"/></svg>
      <span>SEARCH . . .</span>
    </div>
    <div class="abs mail">
      <svg width="12" height="9" viewBox="0 0 12 9"><rect x=".5" y=".5" width="11" height="8" fill="none" stroke="#fff"/><polyline points=".5,.5 6,5 11.5,.5" fill="none" stroke="#fff"/></svg>
      <span>info@vornalto.com</span>
    </div>
  </div>
  <nav class="abs nav">
    <a>Home</a><a>Portfolio</a><a>Online Shop</a><a>Kontakt</a>
  </nav>
  <div class="abs logo-wreath" role="img" aria-label="Florale Linienillustration rund um das Logo"></div>
  <div class="abs logo-plate">VORNALTO</div>
</header>

<section class="abs welcome">
  <div class="abs welcome-box">
    <h1>Willkommen</h1>
    <p>But I must explain to you how all this mistaken idea of denouncing pleasure and praising pain was born and I will give you a complete account of the system, and expound the actual teachings of the great explorer of the truth, the master-builder of human happiness. No one rejects, dislikes, or avoids pleasure itself, because it is pleasure, but because those who do not know how to pursue pleasure rationally encounter consequences that are extremely painful.</p>
    <p>Nor again is there anyone who loves or pursues or desires to obtain pain of itself, because it is pain, but because occasionally circumstances occur in which toil and pain can procure him some great pleasure. To take a trivial example, which of us ever undertakes laborious physical exercise, except to obtain some advantage from it</p>
  </div>
</section>

<section class="abs portfolio">
  <h2>Portfolio</h2>
  <div class="card" style="left:111px;top:151px"><div class="photo" role="img" aria-label="Safranfäden" style="background:radial-gradient(circle,#b0121a 0,#d8282a 60%,#fff 80%)"></div><h3>Safran</h3><div class="btn">MEER INFORMATIE</div></div>
  <div class="card" style="left:362px;top:151px"><div class="photo" role="img" aria-label="Gewürze in Holzschaufeln" style="background:radial-gradient(circle at 55% 55%,#d99a2a 0,#c0602a 40%,#e8ddc8 75%)"></div><h3>Gewürze</h3><div class="btn">MEER INFORMATIE</div></div>
  <div class="card" style="left:612px;top:151px"><div class="photo" role="img" aria-label="Getrocknete Früchte" style="background:radial-gradient(circle,#e08a20 0,#7a3a2a 50%,#f4efe6 80%)"></div><h3>Trockenfrüchte</h3><div class="btn">MEER INFORMATIE</div></div>
  <div class="card" style="left:862px;top:151px"><div class="photo" role="img" aria-label="Mörser mit frischen Kräutern" style="background:radial-gradient(circle at 50% 60%,#3a6a2a 0,#4c8a38 45%,#f4f4f0 75%)"></div><h3>Kräuter</h3><div class="btn">MEER INFORMATIE</div></div>
  <div class="card" style="left:111px;top:507px"><div class="photo" role="img" aria-label="Pistazien" style="background:radial-gradient(circle,#b89a6a 0,#7a9a3a 40%,#fff 72%)"></div><h3>Pistazien</h3><div class="btn">MEER INFORMATIE</div></div>
  <div class="card" style="left:362px;top:507px"><div class="photo" role="img" aria-label="Getrocknete Teeblätter mit frischer Minze" style="background:radial-gradient(circle at 50% 60%,#3a3a30 0,#3c7a30 45%,#fff 75%)"></div><h3>Tee</h3><div class="btn">MEER INFORMATIE</div></div>
  <div class="card" style="left:612px;top:507px"><div class="photo" role="img" aria-label="Sonnenblumen und Ölflasche" style="background:radial-gradient(circle,#e8b010 0,#f2c21a 45%,#fff 78%)"></div><h3>Öl</h3><div class="btn">MEER INFORMATIE</div></div>
  <div class="card" style="left:862px;top:507px"><div class="photo" role="img" aria-label="Weißer Reis" style="background:radial-gradient(circle,#f2f2f0 0,#dcdcd8 50%,#fff 80%)"></div><h3>Reis</h3><div class="btn">MEER INFORMATIE</div></div>
</section>

<section class="abs contact">
  <div class="abs branch" style="left:78px" role="img" aria-label="Florale Zweigillustration in weißen Linien"></div>
  <div class="abs branch" style="left:861px" role="img" aria-label="Florale Zweigillustration in weißen Linien"></div>
  <div class="abs contact-frame"></div>
  <h2>Kontakt</h2>
  <div class="abs rule" style="left:372px;width:142px"></div>
  <div class="abs rule" style="left:686px;width:142px"></div>
  <div class="abs gold-dash"></div>
  <p class="lead">Lorem Ipsum is simply dummy text of the printing and typesetting</p>
  <div class="abs field" style="left:358px;top:265px;width:234px">First Name:</div>
  <div class="abs field" style="left:610px;top:265px;width:234px">Last Name:</div>
  <div class="abs field" style="left:358px;top:325px;width:486px">Email Address:</div>
  <div class="abs join">JOIN</div>
</section>

<footer class="abs footer">
  <div class="abs rows">
    <div class="abs footnav">
      <span style="width:142px;text-align:center;padding-left:20px">Home</span>
      <span style="width:30px">|</span>
      <span style="width:140px;text-align:center">Portfolio</span>
      <span style="width:50px">|</span>
      <span style="width:130px;text-align:center">Online Shop</span>
      <span style="width:70px;text-align:center">|</span>
      <span style="width:90px;text-align:center">Kontakt</span>
    </div>
    <div class="abs social">
      <i class="dark"><svg width="9" height="6" viewBox="0 0 9 6"><polyline points="1,5 4.5,1.5 8,5" fill="none" stroke="#fff" stroke-width="1.4"/></svg></i>
      <i></i><i></i><i></i><i class="accent"></i>
    </div>
    <div class="abs info">
      <div style="width:237px">Addrss: 14 Kaiweg<br>20457 Hamburg</div>
      <div style="width:251px">Email: info@vornalto.com</div>
      <div style="width:250px">Phone: 040-555-0182</div>
      <div style="width:240px">Fax: 040-555-0183</div>
    </div>
  </div>
</footer>

</body>
</html>
```